Business card for a new cabinet shop company named Marlowe Cabinets for high end cabinets

Design a business card, thinking dark rich green with colours to speak of high end luxury ie; cream, gold, black possibly

Peter Lindqvar
Director Craftsman
Email: info@marlowecabinets.com.au
Instagram : @marlowe.cabinets

```html
<!DOCTYPE html>
<html lang="en">
<head>
<meta charset="utf-8">
<title>Marlowe Cabinets – Business Card</title>
<link rel="stylesheet" href="https://fonts.googleapis.com/css2?family=Montserrat:wght@400;500;700&display=swap">
<style>
  :root {
    --backdrop: #3b3b3c;
    --card-white: #ffffff;
    --card-black: #262626;
    --gold: #c4a35a;
    --ink: #1f1f1f;
    --paper-text: #ffffff;
  }
  * { box-sizing: border-box; margin: 0; padding: 0; }
  html, body {
    width: 1200px;
    height: 1200px;
    overflow: hidden;
    background: var(--backdrop);
    font-family: "Montserrat", sans-serif;
  }
  .stage {
    width: 1200px;
    height: 1200px;
    display: flex;
    flex-direction: column;
    align-items: center;
    justify-content: center;
    gap: 44px;
  }
  .card {
    position: relative;
    width: 900px;
    height: 514px;
    border-radius: 40px;
    border: 3px solid var(--gold);
    overflow: hidden;
  }
  .card--front { background: var(--card-white); }
  .card--back { background: var(--card-black); }

  .brand {
    position: absolute;
    display: flex;
    align-items: center;
    gap: 22px;
  }
  .brand__mark {
    width: 54px;
    height: 54px;
    border: 4px solid var(--gold);
    flex: none;
  }
  .brand__name {
    font-weight: 500;
    color: var(--gold);
    letter-spacing: 0.04em;
    white-space: nowrap;
  }
  .card--front .brand { left: 150px; top: 120px; }
  .card--front .brand__name { font-size: 56px; }
  .card--back .brand { left: 50%; top: 50%; transform: translate(-50%, -50%); }
  .card--back .brand__name { font-size: 64px; }

  .divider {
    position: absolute;
    left: 150px;
    right: 70px;
    top: 298px;
    height: 2px;
    background: var(--gold);
  }
  .person {
    position: absolute;
    left: 150px;
    top: 230px;
  }
  .person__name {
    font-weight: 700;
    font-size: 34px;
    color: var(--gold);
    text-transform: uppercase;
    letter-spacing: 0.01em;
    line-height: 1;
  }
  .person__role {
    font-size: 22px;
    color: var(--ink);
    margin-top: 6px;
    line-height: 1;
  }
  .contact {
    position: absolute;
    left: 150px;
    top: 330px;
    list-style: none;
    display: flex;
    flex-direction: column;
    gap: 16px;
  }
  .contact__item {
    display: flex;
    align-items: center;
    gap: 16px;
    font-size: 24px;
    color: var(--ink);
  }
  .contact__icon {
    width: 28px;
    height: 28px;
    flex: none;
  }
  .contact__icon--square {
    border: 3px solid var(--gold);
    border-radius: 6px;
  }
</style>
</head>
<body>
  <main class="stage">
    <section class="card card--front" aria-label="Business card front">
      <div class="brand">
        <span class="brand__mark"></span>
        <span class="brand__name">Marlowe Cabinets</span>
      </div>
      <div class="person">
        <p class="person__name">Peter Lindqvar</p>
        <p class="person__role">Director Craftsman</p>
      </div>
      <div class="divider"></div>
      <ul class="contact">
        <li class="contact__item">
          <span class="contact__icon contact__icon--square"></span>
          @marlowe.cabinets
        </li>
        <li class="contact__item">
          <svg class="contact__icon" viewBox="0 0 28 28" aria-hidden="true">
            <rect x="2" y="6" width="24" height="16" fill="var(--gold)"/>
            <path d="M2 6 L14 15 L26 6" fill="none" stroke="#ffffff" stroke-width="2"/>
          </svg>
          info@marlowecabinets.com.au
        </li>
      </ul>
    </section>

    <section class="card card--back" aria-label="Business card back">
      <div class="brand">
        <span class="brand__mark"></span>
        <span class="brand__name">Marlowe Cabinets</span>
      </div>
    </section>
  </main>
</body>
</html>
```